Aged Care Home - TM

We need a website design for a homepage and a content page for an aged care home in Kelmore. I have attached a detailed design/content brief and their logo to be used in concepts. Also bear in mind this design will be skinned for Dot Net Nuke 4.8.2 so design needs to be used on this content management system.

The following elements are required in the design:

• Phone number will be featured in banner on each page 07 5281 6637

• An area for a large flash banner of rotating images on homepage

• Images need to reflect credibility, professionalism and caring (just use some example images for now as we’ll need to source some)

• Large logo in banner as well

• Some icons on homepage to include:

• Download Application Form

• Admission Kit

• Contact Us

```html
<!DOCTYPE html>
<html lang="en">
<head>
<meta charset="utf-8">
<title>The Tom Marsh Home – Aged Care Facility</title>
<link rel="stylesheet" href="https://fonts.googleapis.com/css2?family=Arimo:wght@400;700&family=Cabin:wght@400;500&display=swap">
<style>
:root{
  --navy:#2b3a8e;
  --lavender:#a9b1d4;
  --lavender-dark:#8f98c4;
  --mist:#dfe2ef;
  --page:#f6f7fb;
  --white:#ffffff;
  --headline:#aab0d3;
  --muted:#9aa2c8;
}
*{margin:0;padding:0;box-sizing:border-box}
html,body{width:1200px;height:900px;overflow:hidden}
body{position:relative;background:var(--page);font-family:'Arimo',Arial,sans-serif;color:var(--navy)}
.page{position:absolute;left:47px;top:0;width:1103px;height:900px;background:linear-gradient(#f6f7fb 0,#f6f7fb 117px,#e6e9f3 180px,#f3f4f9 560px,#ffffff 860px)}
.brand{position:absolute;display:flex;align-items:center;gap:10px;font-family:'Cabin',Arial,sans-serif;color:var(--navy);font-weight:500;white-space:nowrap}
.brand-dot{width:14px;height:14px;border-radius:50%;background:var(--navy)}
.brand--header{left:90px;top:24px;font-size:20px}
.tagline{position:absolute;left:403px;top:28px;font-size:33px;font-weight:700;color:var(--headline);text-shadow:0 1px 0 #fff,0 0 2px #8d95c1;white-space:nowrap}
.phone{position:absolute;left:502px;top:80px;font-size:19px;color:var(--muted)}
.search{position:absolute;left:783px;top:34px;width:268px;height:24px;border-radius:12px;background:#fff;box-shadow:inset 0 1px 3px #c8cce0;font-size:14px;padding:4px 22px;color:var(--navy)}
.search-btn{position:absolute;left:1061px;top:34px;width:47px;height:24px;border-radius:12px;background:linear-gradient(#c3c8e2,#9aa2cb);border:1px solid #8c94c2}
.search-btn svg{position:absolute;left:14px;top:4px}
.newsletter{position:absolute;left:775px;top:78px;width:340px;height:41px;background:#fff;border:1px solid #c9cde2;border-bottom:none;border-radius:14px 14px 0 0;display:flex;align-items:center;justify-content:center;gap:14px;font-size:19px;color:var(--navy)}
.newsletter em{font-style:normal;color:var(--muted)}
.header-rule{position:absolute;left:47px;top:117px;width:1103px;height:1px;background:#c9cde2}
.nav{position:absolute;left:78px;top:131px;width:1040px;height:36px;display:flex;box-shadow:0 2px 4px rgba(120,130,180,.4)}
.nav .brand{position:static;width:303px;height:36px;background:#fff;padding-left:44px;font-size:17px}
.nav ul{list-style:none;display:flex;flex:1;background:linear-gradient(#bcc2e0,#a3abd2)}
.nav li{flex:auto;color:#fff;font-size:19px;line-height:36px;text-align:center;border-left:1px solid #d2d6ea;white-space:nowrap}
.hero{position:absolute;left:77px;top:206px;width:1036px;height:330px;border:1px solid #c2c7df;border-radius:8px;background:#fff;box-shadow:0 6px 12px rgba(150,160,200,.3)}
.hero-stage{position:absolute;left:4px;top:4px;width:816px;height:320px;background:linear-gradient(90deg,#e6e3e0 0,#d9dbe8 45%,#d6daeb 100%);border-radius:4px 0 0 4px;overflow:hidden}
.hero-photo{position:absolute;left:0;top:0;width:464px;height:320px;background:radial-gradient(ellipse at 40% 45%,#d8b7a0 0,#c9b6b0 35%,rgba(214,218,235,0) 72%)}
.hero-title{position:absolute;right:18px;top:80px;text-align:right;font-size:56px;line-height:60px;font-weight:400;color:var(--headline);text-shadow:0 0 1px #6f78ad,0 1px 0 #fff;white-space:nowrap}
.hero-side{position:absolute;left:820px;top:4px;width:212px;height:320px;background:#e5e7f1}
.hero-side .panel{position:absolute;left:0;top:0;width:212px;height:188px;background:linear-gradient(#d4d8ea,#e1e4f0);display:flex;align-items:flex-end;justify-content:center;padding-bottom:18px}
.hero-side .brand{position:static;font-size:16px}
.action{position:absolute;left:8px;width:198px;height:46px;background:linear-gradient(#c4c9e4,#a1a9d1);border:1px solid #fff;box-shadow:0 1px 3px rgba(100,110,160,.4);color:#fff;font-size:19px;display:flex;align-items:center;gap:12px;padding-left:12px;white-space:nowrap}
.action i{width:22px;height:22px;border-radius:50%;background:linear-gradient(#eef0f8,#b3b9da);display:flex;align-items:center;justify-content:center}
.action--kit{top:205px}
.action--form{top:270px}
.intro{position:absolute;left:108px;top:603px;width:770px;font-size:16.5px;line-height:20px;color:var(--navy)}
.intro p+p{margin-top:20px}
.careers{position:absolute;left:902px;top:557px;width:207px;height:264px;background:#e1e4f0}
.careers h2{height:34px;background:linear-gradient(#bcc2e0,#a3abd2);color:#fff;font-weight:400;font-size:19px;line-height:34px;text-align:center;border:1px solid #fff}
.job{position:absolute;left:6px;width:195px;height:67px;background:linear-gradient(#c0c6e2,#a7afd4);border:1px solid #fff;padding:4px 8px;color:#fff;overflow:hidden}
.job h3{font-size:12px;font-weight:700;line-height:13px}
.job p{font-size:9px;line-height:12px}
.job a{color:var(--navy)}
.job--1{top:40px}
.job--2{top:114px}
.job--3{top:188px}
.footer{position:absolute;left:47px;top:867px;width:1103px;height:33px;background:var(--lavender);text-align:center;font-size:10.5px;line-height:12px;padding-top:7px;color:var(--navy)}
</style>
</head>
<body>
<div class="page"></div>

<header>
  <div class="brand brand--header"><span class="brand-dot"></span>the TOM MARSH HOME</div>
  <div class="tagline">Aged Care Facility</div>
  <div class="phone">call us: 07 5281 6637</div>
  <div class="search">Search</div>
  <div class="search-btn">
    <svg width="18" height="15" viewBox="0 0 18 15"><circle cx="11" cy="6" r="4.5" fill="none" stroke="#fff" stroke-width="2"/><line x1="7.5" y1="9" x2="2" y2="13" stroke="#fff" stroke-width="2.5"/></svg>
  </div>
  <div class="newsletter">
    <svg width="36" height="22" viewBox="0 0 36 22"><rect x="1" y="1" width="34" height="20" fill="#e3e6f2" stroke="#b3b9da"/><path d="M1 1 L18 13 L35 1" fill="none" stroke="#b3b9da"/></svg>
    <span>Sign up <em>for newsletter</em></span>
  </div>
</header>
<div class="header-rule"></div>

<nav class="nav">
  <div class="brand"><span class="brand-dot"></span>the TOM MARSH HOME</div>
  <ul>
    <li>Home</li><li>About Us</li><li>Accommodation</li><li>Financial Info</li><li>Philosophy of Care</li><li>Contact Us</li>
  </ul>
</nav>

<section class="hero">
  <div class="hero-stage">
    <div class="hero-photo" role="img" aria-label="Photo of two smiling elderly men embracing"></div>
    <h1 class="hero-title">WE BUILD<br>ON STRONG<br>RELATIONSHIP</h1>
  </div>
  <aside class="hero-side">
    <div class="panel"><div class="brand"><span class="brand-dot"></span>the TOM MARSH HOME</div></div>
    <div class="action action--kit"><i><svg width="10" height="12" viewBox="0 0 10 12"><path d="M5 0v8M1 5l4 4 4-4" fill="none" stroke="#8f98c4" stroke-width="2"/></svg></i>Admission Kit</div>
    <div class="action action--form"><i><svg width="10" height="12" viewBox="0 0 10 12"><path d="M5 0v8M1 5l4 4 4-4" fill="none" stroke="#8f98c4" stroke-width="2"/></svg></i>Application Form</div>
  </aside>
</section>

<main class="intro">
  <p>The Tom Marsh Home, situated in the riverside Kelmore Suburb of Ashford, has a long history of providing accommodation to people of the community. The Ashford Lodge, as it was known during World War II, was completely rebuilt in 1979 when the Senior Residents Welfare Association was formed.</p>
  <p>Over the years refurbishments and renovations to the home have resulted in the establishment of a modern, comfortable facility which is a registered charitable organization, aligned to no other group and is administered by a voluntary board of directors.</p>
</main>

<aside class="careers">
  <h2>career opportunities</h2>
  <div class="job job--1"><h3>Lorem ipsum</h3><p>Lorem ipsum dolor sit amet, consectetur adipisicing elit, sed do eiusmod tempor incididunt ut labore et dolore magna aliqua. Ut enim ad minim <a>...more...</a></p></div>
  <div class="job job--2"><h3>Lorem ipsum</h3><p>Lorem ipsum dolor sit amet, consectetur adipisicing elit, sed do eiusmod tempor incididunt ut labore et dolore magna aliqua. Ut enim ad minim <a>...more...</a></p></div>
  <div class="job job--3"><h3>Lorem ipsum</h3><p>Lorem ipsum dolor sit amet, consectetur adipisicing elit, sed do eiusmod tempor incididunt ut labore et dolore magna aliqua. Ut enim ad minim <a>...more...</a></p></div>
</aside>

<footer class="footer">
  All content is 2009 by tom marsh home. All rights reserved.<br>
  18 Riverview Street, P O Box 214, ASHFORD 4412; tel.: 07 5281 663
</footer>
</body>
</html>
```